International Charity Single Needs Artwork.

Bright and Near (www.brightandnear.com) began in June 2016, as a response to divisive events worldwide. I wrote the song 'Open Hands', which has been recorded around the world, featuring an array of artists and choirs, due for release on June 16th. A preview of the single is here:

https://vidshare.example/Qx7LpTz2wKe

I would suggest either something very simple (Bright and Near - Open Hands, on basic background), or something which incorporates images of the many participants - refugee choir, Vietnamese choir, solo singers and players. I can provide images for the latter, of course.

Target Market(s)

Mainstream Music Market.

Logo Text

Bright and Near

Font styles to use
Sans Serif

Colors

Designer to choose colors to be used in the design.

Requirements
Must have
• A thumbnail. This is for online release (not CD), so it just needs to be a square thumbnail.
Nice to have
• I've attached several thumbnails from the video, just as ideas. It may be possible to create a collage of lots of participants, to give the sense of scale/international tapestry. Alternatively, you could try using just one image.
• These images may not be necessary though. I would otherwise be very interested to see your own creative designs, inspired by the project. They could be quite simple - depicting calm, humanity, friendship. Or they could be more ambitious, and suggest a global tapestry. Looking forward! I hope you enjoy.

```html
<!DOCTYPE html>
<html lang="en">
<head>
<meta charset="utf-8">
<title>Bright and Near – Open Hands</title>
<link rel="stylesheet" href="https://fonts.googleapis.com/css2?family=Yellowtail&family=Poiret+One&display=swap">
<style>
  :root {
    --paper-light: #eef0ea;
    --paper-mid: #d9ddd6;
    --paper-blue: #c9d6d8;
    --skin-gold: #b08a3a;
    --skin-olive: #7e6f3c;
    --skin-deep: #4a2f24;
    --skin-rose: #c88f78;
    --skin-copper: #a2482a;
    --title-red: #e2202e;
    --title-grey: #3b3b3d;
    --ink: #1e1e20;
  }
  * { margin: 0; padding: 0; box-sizing: border-box; }
  html, body { width: 1200px; height: 1200px; overflow: hidden; }
  body { background: var(--paper-light); }
  .cover {
    position: relative;
    width: 1200px;
    height: 1200px;
    overflow: hidden;
    background:
      radial-gradient(circle at 20% 15%, #f3efd8 0%, transparent 45%),
      radial-gradient(circle at 80% 80%, var(--paper-blue) 0%, transparent 55%),
      linear-gradient(135deg, var(--paper-light), var(--paper-mid));
  }
  .cover__artwork {
    position: absolute;
    inset: 0;
    width: 1200px;
    height: 1200px;
  }
  .title {
    position: absolute;
    left: 0;
    top: 0;
    width: 1200px;
    height: 1200px;
    font-family: "Yellowtail", cursive;
    pointer-events: none;
  }
  .title__line {
    position: absolute;
    white-space: nowrap;
    line-height: 1;
  }
  .title__main {
    left: 338px;
    top: 400px;
    font-size: 200px;
    color: var(--title-red);
  }
  .title__joiner {
    left: 340px;
    top: 598px;
    font-size: 120px;
    color: var(--title-grey);
  }
  .title__second {
    left: 530px;
    top: 572px;
    font-size: 190px;
    color: var(--title-red);
  }
  .song-name {
    position: absolute;
    left: 126px;
    top: 1128px;
    font-family: "Poiret One", sans-serif;
    font-size: 52px;
    letter-spacing: 6px;
    color: var(--ink);
    text-transform: uppercase;
    line-height: 1;
  }
</style>
</head>
<body>
<main class="cover">
  <svg class="cover__artwork" viewBox="0 0 1200 1200" role="img" aria-label="Photograph of many hands of different skin tones joined together to form a circle around the title">
    <defs>
      <radialGradient id="hands-tone" cx="600" cy="640" r="620" gradientUnits="userSpaceOnUse">
        <stop offset="0.48" stop-color="var(--skin-rose)"/>
        <stop offset="0.7" stop-color="var(--skin-olive)"/>
        <stop offset="1" stop-color="var(--skin-deep)" stop-opacity="0.6"/>
      </radialGradient>
      <linearGradient id="hands-warmth" x1="0" y1="0" x2="1" y2="1">
        <stop offset="0" stop-color="var(--skin-gold)" stop-opacity="0.55"/>
        <stop offset="0.5" stop-color="var(--skin-deep)" stop-opacity="0.15"/>
        <stop offset="1" stop-color="var(--skin-copper)" stop-opacity="0.55"/>
      </linearGradient>
      <mask id="ring-mask">
        <rect width="1200" height="1200" fill="black"/>
        <circle cx="600" cy="640" r="540" fill="white"/>
        <circle cx="600" cy="640" r="300" fill="black"/>
      </mask>
    </defs>
    <g mask="url(#ring-mask)">
      <rect width="1200" height="1200" fill="url(#hands-tone)" opacity="0.85"/>
      <rect width="1200" height="1200" fill="url(#hands-warmth)"/>
    </g>
  </svg>

  <h1 class="title">
    <span class="title__line title__main">Bright</span>
    <span class="title__line title__joiner">and</span>
    <span class="title__line title__second">Near</span>
  </h1>

  <p class="song-name">Open Hands</p>
</main>
</body>
</html>
```